Tre Nuvole Leaf Design Business Card/Hang Tag

Design a 3.5" X 2" (Leaf Shaped-See Files) Business Card/ Hang Tag that will have our Business Logo and Info on the Front, and will have On-Line Delivery Logos and Info on the Rear.

```html
<!DOCTYPE html>
<html lang="en">
<head>
<meta charset="utf-8">
<title>Tre Nuvole Leaf Business Card</title>
<link rel="stylesheet" href="https://fonts.googleapis.com/css2?family=Berkshire+Swash&family=Sansita:ital,wght@0,700;1,800&family=Cormorant+Garamond:ital,wght@1,500&family=Open+Sans:wght@400&display=swap">
<style>
:root{
  --page:#ededed;
  --red:#c4161c;
  --deep-red:#a8121a;
  --green:#1f6b2a;
  --ink:#1d1d1d;
  --rose-1:#f3d3da;
  --rose-2:#e9c3cc;
  --leaf-1:#dfe8d6;
  --leaf-2:#cfdcc6;
  --path:#eeeeea;
  --badge:#ffffff;
  --badge-line:#d9d9d9;
}
*{margin:0;padding:0;box-sizing:border-box}
html,body{width:1200px;height:757px;overflow:hidden;background:var(--page)}
.canvas{position:relative;width:1200px;height:757px;background:var(--page)}
.card{position:absolute;top:198px;width:512px;height:296px;overflow:hidden}
.card--front{left:77px;border-radius:0 110px 0 110px}
.card--back{left:623px;border-radius:110px 0 110px 0}
.garden-photo{position:absolute;inset:0;
  background:
    radial-gradient(ellipse 60px 150px at 50% 75%, var(--path) 0%, transparent 100%),
    radial-gradient(ellipse at 15% 30%, var(--rose-2) 0%, transparent 55%),
    radial-gradient(ellipse at 85% 30%, var(--rose-2) 0%, transparent 55%),
    linear-gradient(180deg, var(--rose-1) 0%, var(--rose-1) 45%, var(--leaf-1) 75%, var(--leaf-2) 100%);}
.content{position:absolute;inset:0;text-align:center}
.brand{position:absolute;left:0;right:0;top:86px;color:var(--red);
  font-family:"Berkshire Swash",cursive;font-size:36px;line-height:1.05}
.brand span{display:block;font-size:22px}
.website{position:absolute;left:0;right:0;top:192px;color:var(--red);
  font-family:"Sansita",sans-serif;font-style:italic;font-weight:800;font-size:19px;letter-spacing:.2px}
.rule{position:absolute;left:126px;width:268px;top:232px;height:2px;background:var(--green)}
.address{position:absolute;left:0;right:0;top:236px;color:var(--green);
  font-family:"Sansita",sans-serif;font-weight:700;font-size:13.5px;line-height:15px}
.tagline{position:absolute;left:0;right:0;top:194px;color:var(--red);
  font-family:"Berkshire Swash",cursive;font-size:20px}
.label{position:absolute;top:234px;color:var(--deep-red);
  font-family:"Cormorant Garamond",serif;font-style:italic;font-weight:500;font-size:11px;text-decoration:underline}
.label--delivery{left:58px}
.label--hours{left:318px}
.partners{position:absolute;left:53px;top:256px;display:flex;gap:6px}
.partner-badge{height:29px;border-radius:7px;background:var(--badge);border:1px solid var(--badge-line)}
.partner-badge--wide{width:49px}
.partner-badge--mid{width:42px}
.partner-badge--small{width:31px}
.hours{position:absolute;left:278px;width:120px;top:255px;color:var(--ink);
  font-family:"Open Sans",sans-serif;font-size:10.5px;line-height:17px}
</style>
</head>
<body>
<main class="canvas">
  <section class="card card--front">
    <div class="garden-photo" role="img" aria-label="Soft rose garden archway with a path between flowering hedges"></div>
    <div class="content">
      <h1 class="brand">Tre Nuvole<span>Restaurant</span></h1>
      <p class="website">www.trenuvolerestaurant.com</p>
      <div class="rule"></div>
      <address class="address">127 Linden Avenue<br>Fairhaven, California 94071<br>(555) 014-2289</address>
    </div>
  </section>
  <section class="card card--back">
    <div class="garden-photo" role="img" aria-label="Soft rose garden archway with a path between flowering hedges"></div>
    <div class="content">
      <h1 class="brand">Tre Nuvole<span>Restaurant</span></h1>
      <p class="tagline">Authentic Italian Dining and Take-Out</p>
      <p class="label label--delivery">On-Line Delivery Partners:</p>
      <div class="partners">
        <div class="partner-badge partner-badge--wide"></div>
        <div class="partner-badge partner-badge--mid"></div>
        <div class="partner-badge partner-badge--small"></div>
      </div>
      <p class="label label--hours">Hours:</p>
      <p class="hours">4:00pm to 9:00pm<br>(7 days a week)</p>
    </div>
  </section>
</main>
</body>
</html>
```